Quality Monitoring Company Needs a New Site

We are an established company that has a fair number of clients but the site lacks current design standards that we'd like to keep up with. We'd like to mimic the same style of the site on quorvlinapp.example, belstrum.example, https://tindleworkpays.example/, etc. We'd also like to make sure the designer understands SEO Silos and how it effects the design elements. Attached is the structure that I'd like to follow for the pages. You don't need to design every single sub-page because they'll probably be fairly similar; however, I want to see at least 1 each. Please use the content on our current site for filler areas. Please try to do a good job of understanding what we do so you can use your best judgement on what is needed to be successful. Use our color scheme and the logo should be the side view but I included the AI just in case.
Updates

I am narrowing down on the field of designs that I have received. There are a lot of similarities between the designs I like and don't like. I'd also like to ensure that some of the inner pages get done in the next 5 days so I can see the creativity that is there as well. That is probably what is next -- getting a few inner pages completed so I can see what you can come up with (not based on our current website) because the current "front pages" are all so good and so close.

Industry/Entity Type

Telecommunications

Colors

Designer to choose colors to be used in the design.

Requirements
Must have
• SEO Silo Look and Feel
• Current Colors
Should not have
• No stockphotos whatsoever. NONE.

```html
<!DOCTYPE html>
<html lang="en">
<head>
<meta charset="utf-8">
<title>QualiSpan – Call Center Quality Assurance</title>
<link href="https://fonts.googleapis.com/css2?family=Poppins:wght@400;500;600;700&display=swap" rel="stylesheet">
<style>
:root{
  --blue:#1a9be8;
  --blue-dark:#0f7fc9;
  --navy:#1c2a4d;
  --text:#6b7385;
  --muted:#9aa1b1;
  --line:#e6ebf2;
  --soft:#eef6fd;
  --soft-2:#f6f9fc;
  --white:#ffffff;
  --purple:#8c6ee8;
  --green:#33c28a;
}
*{box-sizing:border-box;margin:0;padding:0}
html,body{width:1200px;height:4356px;overflow:hidden}
body{font-family:"Poppins",sans-serif;color:var(--text);background:var(--white);font-size:13px;line-height:1.7;position:relative}
.section{position:absolute;left:0;width:1200px}
h1,h2,h3,h4{color:var(--navy);font-weight:700;line-height:1.3}
.accent{color:var(--blue)}
.btn{display:inline-block;background:var(--blue);color:var(--white);font-weight:500;font-size:13px;padding:11px 30px;border-radius:24px;box-shadow:0 8px 18px rgba(26,155,232,.3)}
.art{border-radius:24px}

/* nav */
.nav{top:0;height:88px;display:flex;align-items:center;padding:0 60px}
.logo{display:flex;align-items:center;gap:8px;font-weight:700;font-size:22px;color:var(--navy)}
.logo-dot{width:14px;height:14px;border-radius:50%;background:var(--blue)}
.nav-links{display:flex;gap:34px;margin-left:auto;margin-right:60px;font-size:13px;color:var(--navy)}
.nav-links .active{color:var(--blue);border-bottom:2px solid var(--blue);padding-bottom:4px}
.nav .btn{padding:8px 30px}

/* hero */
.hero{top:88px;height:392px}
.hero-copy{position:absolute;left:60px;top:60px;width:520px}
.hero-copy h1{font-size:28px}
.hero-copy p{margin-top:20px;font-size:12.5px}
.hero-copy .btn{margin-top:38px}
.hero-art{position:absolute;left:700px;top:10px;width:460px;height:360px;background:linear-gradient(135deg,#dff0fc,#b9dcf5);border-radius:180px 30px 180px 60px}

/* intro */
.intro{top:560px;height:220px;text-align:center}
.intro h2{font-size:30px}
.intro p{width:840px;margin:24px auto 0;font-size:12.5px}

/* problem */
.problem{top:780px;height:420px}
.problem-art{position:absolute;left:100px;top:0;width:400px;height:400px;border-radius:50%;background:radial-gradient(circle,#d6ecfb,#eef7fe)}
.problem-copy{position:absolute;left:580px;top:20px;width:560px}
.problem-copy p{font-size:12.5px;margin-bottom:12px}
.problem-copy .lead{font-size:15px;color:var(--navy);font-weight:500}
.ticks{list-style:none;margin-bottom:14px}
.ticks li{position:relative;padding-left:22px;font-size:12.5px}
.ticks li::before{content:"";position:absolute;left:4px;top:9px;width:7px;height:7px;border-radius:50%;background:var(--blue)}

/* services */
.services{top:1280px;height:720px;text-align:center}
.services h2{font-size:30px}
.services-board{position:absolute;left:100px;top:170px;width:1000px;height:540px;background:var(--soft-2);border-radius:8px}
.cards{position:absolute;left:140px;top:200px;display:flex;gap:20px}
.card{width:293px;height:480px;background:var(--white);border-radius:6px;box-shadow:0 10px 28px rgba(28,42,77,.08);padding:34px 28px;text-align:left}
.card.featured{background:var(--blue);margin-top:-16px;height:512px}
.card.featured h3,.card.featured p{color:var(--white)}
.card-icon{width:46px;height:46px;border-radius:10px;background:var(--soft);margin-bottom:22px}
.card.featured .card-icon{background:rgba(255,255,255,.25)}
.card h3{font-size:16px;margin-bottom:16px}
.card p{font-size:12px}

/* why */
.why{top:2030px;height:640px}
.why-art{position:absolute;left:60px;top:90px;width:500px;height:420px;background:linear-gradient(160deg,#e4f2fc,#f7fbff)}
.why-copy{position:absolute;left:580px;top:40px;width:560px}
.why-copy h2{font-size:28px;margin-bottom:24px}
.acc-item{border-bottom:1px solid var(--line);padding:12px 0;font-size:13.5px;font-weight:500;color:var(--navy);display:flex;justify-content:space-between}
.acc-item.open{color:var(--blue);border-bottom:2px solid var(--blue)}
.acc-body{font-size:12px;padding:14px 0 10px}
.chev{color:var(--muted)}

/* news */
.news{top:2700px;height:540px;text-align:center}
.news h2{font-size:30px}
.news-row{position:absolute;left:220px;top:180px;display:flex;gap:20px}
.news-card{width:240px;height:320px;background:var(--white);border-radius:6px;box-shadow:0 10px 28px rgba(28,42,77,.08);padding:26px 24px;text-align:left;position:relative}
.news-card.featured{background:var(--blue)}
.news-card.featured h3,.news-card.featured p,.news-card.featured .arrow{color:var(--white)}
.tag{display:inline-block;font-size:10px;color:var(--white);padding:3px 12px;border-radius:3px;margin-bottom:60px}
.tag.purple{background:var(--purple)}
.tag.white{background:var(--white);color:var(--blue)}
.tag.green{background:var(--green)}
.news-card h3{font-size:15px;margin-bottom:12px}
.news-card p{font-size:11.5px}
.arrow{position:absolute;left:24px;bottom:22px;font-size:18px;color:var(--blue)}

/* hybrid */
.hybrid{top:3240px;height:580px}
.hybrid-art{position:absolute;left:120px;top:20px;width:440px;height:520px;background:linear-gradient(180deg,#e8f4fd,#cfe7f9);border-radius:220px 220px 24px 24px}
.hybrid-copy{position:absolute;left:620px;top:90px;width:500px}
.hybrid-copy h2{font-size:28px;margin-bottom:20px}
.hybrid-copy p{font-size:12.5px;margin-bottom:14px}
.hybrid-copy .btn{margin-top:16px}

/* proof */
.proof{top:3820px;height:330px;background:linear-gradient(180deg,var(--white),var(--soft) 40%,#e3f1fc)}
.proof-copy{position:absolute;left:120px;top:120px;width:440px}
.proof-copy h2{font-size:28px;margin-bottom:16px}
.proof-copy p{font-size:12px;margin-bottom:10px}
.proof-copy .btn{margin-top:12px}
.dash{position:absolute;left:600px;top:40px;width:560px;height:270px;background:var(--white);border-radius:6px;box-shadow:0 14px 36px rgba(28,42,77,.14);overflow:hidden}

/* footer */
.footer{top:4150px;height:170px;display:flex;padding:28px 220px 0 220px;gap:80px}
.footer .logo{font-size:20px;margin-bottom:14px}
.footer-info{font-size:11px;line-height:1.8}
.footer-info .link{color:var(--blue)}
.footer-col h4{font-size:13px;margin-bottom:10px}
.footer-col ul{list-style:none;font-size:11px;line-height:1.9}
.social{display:flex;gap:10px;margin-top:10px}
.social span{width:14px;height:14px;border-radius:50%;background:var(--navy)}
.copyright{top:4320px;height:36px;border-top:1px solid var(--line);text-align:center;font-size:10.5px;line-height:36px;color:var(--muted)}
</style>
</head>
<body>

<header class="section nav">
  <div class="logo"><span class="logo-dot"></span>QualiSpan</div>
  <nav class="nav-links">
    <span class="active">Home</span><span>Services</span><span>Speech Vision</span><span>Pricing</span><span>About</span><span>Blog</span><span>Contact</span>
  </nav>
  <span class="btn">Login</span>
</header>

<section class="section hero">
  <div class="hero-copy">
    <h1>When was the last time Vela delighted you with a satisfying &amp; surprising answer or action?</h1>
    <p><span class="accent">QualiSpan</span> is combining speech and human insight with artificial intelligence to give you a clear and complete picture of every customer call, so your team can act on what really happens in the conversation.</p>
    <span class="btn">Get Started</span>
  </div>
  <div class="hero-art art" role="img" aria-label="Illustration of a call center agent with headset beside floating chat panels"></div>
</section>

<section class="section intro">
  <h2>We are an affordable, accurate, and fully scalable<br><span class="accent">Call Center Quality Assurance Agency.</span></h2>
  <p>QualiSpan is born of the simple understanding that accurate and scalable third party call center QA services are expensive and time consuming. Fortunately, using powerful tools and a team of trained reviewers, we make it possible to score every single call with consistent results and thoughtful feedback, at a fraction of the cost.</p>
</section>

<section class="section problem">
  <div class="problem-art" role="img" aria-label="Illustration of agents on calls connected by speech bubbles"></div>
  <div class="problem-copy">
    <p class="lead">Unfortunately for many QA services, Call Center Quality Assurance is best summarized as one of three options:</p>
    <ul class="ticks">
      <li>Thinly staffed internal teams reviewing a small random sample</li>
      <li>Hiring expensive specialists to review every call</li>
      <li>Buying basic software that flags keywords with little context</li>
    </ul>
    <p class="lead">While all of these approaches are very common, it's easy to see why they are not effective:</p>
    <ul class="ticks">
      <li>Internal review teams rarely get through enough calls to matter</li>
      <li>Hiring more staff drives cost far beyond the value returned</li>
      <li>Plain software misses tone, intent and the real customer story</li>
    </ul>
    <p>At QualiSpan, we believe the key to accurate, scalable and affordable third party QA lies in a blended approach: trained people and smart speech tools working together on every call.</p>
  </div>
</section>

<section class="section services">
  <h2>We are an affordable, accurate, and fully scalable<br><span class="accent">Call Center Quality Assurance Agency.</span></h2>
  <div class="services-board"></div>
  <div class="cards">
    <article class="card">
      <div class="card-icon"></div>
      <h3>Evaluating and Scoring Agent-Customer Interactions</h3>
      <p>Every call your agents handle becomes a clear, scored record. Our reviewers listen for greeting, empathy, accuracy and resolution, then return detailed scorecards that show where each agent shines and where coaching will help most. Results arrive daily so supervisors can act while the call is still fresh.</p>
    </article>
    <article class="card featured">
      <div class="card-icon"></div>
      <h3>Identifying Key Behaviors and Procedures that Drive Sales</h3>
      <p>We look closely at the calls that close and the calls that do not. By matching outcomes with behaviors, we show which phrases, offers and steps lead to a sale, so your scripts and training can focus on what truly moves customers to say yes.</p>
    </article>
    <article class="card">
      <div class="card-icon"></div>
      <h3>Keeping Call Centers Compliant</h3>
      <p>Regulated industries cannot afford a missed disclosure. We check each call against your required statements and flag any gap within hours, giving your compliance team a full trail of reviewed calls and a clear view of risk across every agent and campaign.</p>
    </article>
  </div>
</section>

<section class="section why">
  <div class="why-art art" role="img" aria-label="Illustration of an agent at a desk with a laptop and a headset icon"></div>
  <div class="why-copy">
    <h2>Why Choose QualiSpan for your<br>Call Center QA Needs?</h2>
    <div class="acc-item open"><span>We Provide Affordable &amp; Cost Effective Call Center QA Services</span><span class="chev">–</span></div>
    <p class="acc-body">Scoring all your calls no longer means a large budget. Our blended model keeps cost per call low while every review is read by a trained person, so you gain full coverage, useful coaching notes and steady quality without growing your internal team.</p>
    <div class="acc-item"><span>Our Human Analysts Can Capture What QA Software Cannot</span><span class="chev">+</span></div>
    <div class="acc-item"><span>We Customize Score Cards to Your Industry</span><span class="chev">+</span></div>
    <div class="acc-item"><span>We'll Give You the Best View of Your Call Center</span><span class="chev">+</span></div>
  </div>
</section>

<section class="section news">
  <h2>Check out our latest<br>news &amp; articles</h2>
  <div class="news-row">
    <article class="news-card">
      <span class="tag purple">Coaching</span>
      <h3>5 Great Call Center Supervisor Skills</h3>
      <p>Simple ways a team lead can lift morale and scores in a single week.</p>
      <span class="arrow">→</span>
    </article>
    <article class="news-card featured">
      <span class="tag white">Training</span>
      <h3>7 Important Call Center Skills For Agents</h3>
      <p>The core habits that turn a good phone agent into a great one.</p>
      <span class="arrow">→</span>
    </article>
    <article class="news-card">
      <span class="tag green">Sales</span>
      <h3>Process vs. Product Sales Solution</h3>
      <p>Why the way you sell can matter more than what you sell today.</p>
      <span class="arrow">→</span>
    </article>
  </div>
</section>

<section class="section hybrid">
  <div class="hybrid-art" role="img" aria-label="Illustration of a friendly robot wearing a headset beside a human agent"></div>
  <div class="hybrid-copy">
    <h2>Ushering The Era of Machine–<br>Human Hybrid</h2>
    <p>QualiSpan is committed to blending real human review with smart speech tools. Machines are fast at sorting and flagging large volumes of calls, while our people bring judgment, context and empathy to each score that reaches your team.</p>
    <p>As a result, you receive the speed and reach of software with the care and accuracy of a trained analyst, giving your managers insight they can trust and act on with confidence every day.</p>
    <span class="btn">Learn more</span>
  </div>
</section>

<section class="section proof">
  <div class="proof-copy">
    <h2>Proof of our Value</h2>
    <p>Organizations that have adopted our blended QA program report higher conversion rates, fewer compliance issues and a clear lift in customer satisfaction within the first months.</p>
    <p>See how our dashboard turns thousands of calls into a few clear numbers.</p>
    <span class="btn">Read more</span>
  </div>
  <svg class="dash" viewBox="0 0 560 270" role="img" aria-label="Quality dashboard table">
    <rect width="560" height="270" fill="#fff"/>
    <rect width="110" height="270" fill="#1c2a4d"/>
    <g fill="#3b4b72"><rect x="16" y="24" width="70" height="8" rx="4"/><rect x="16" y="56" width="60" height="6" rx="3"/><rect x="16" y="76" width="66" height="6" rx="3"/><rect x="16" y="96" width="54" height="6" rx="3"/><rect x="16" y="116" width="62" height="6" rx="3"/></g>
    <rect x="126" y="18" width="120" height="10" rx="5" fill="#1c2a4d"/>
    <g fill="#eef6fd"><rect x="126" y="42" width="98" height="44" rx="4"/><rect x="232" y="42" width="98" height="44" rx="4"/><rect x="338" y="42" width="98" height="44" rx="4"/><rect x="444" y="42" width="98" height="44" rx="4"/></g>
    <g fill="#1a9be8"><rect x="136" y="66" width="40" height="8" rx="4"/><rect x="242" y="66" width="50" height="8" rx="4"/><rect x="348" y="66" width="36" height="8" rx="4"/><rect x="454" y="66" width="46" height="8" rx="4"/></g>
    <rect x="126" y="100" width="416" height="20" fill="#f6f9fc"/>
    <g stroke="#e6ebf2"><line x1="126" y1="144" x2="542" y2="144"/><line x1="126" y1="168" x2="542" y2="168"/><line x1="126" y1="192" x2="542" y2="192"/><line x1="126" y1="216" x2="542" y2="216"/><line x1="126" y1="240" x2="542" y2="240"/></g>
    <g fill="#c9d0dc"><rect x="136" y="128" width="80" height="6" rx="3"/><rect x="136" y="152" width="70" height="6" rx="3"/><rect x="136" y="176" width="86" height="6" rx="3"/><rect x="136" y="200" width="64" height="6" rx="3"/><rect x="136" y="224" width="76" height="6" rx="3"/>
    <rect x="280" y="128" width="50" height="6" rx="3"/><rect x="280" y="152" width="50" height="6" rx="3"/><rect x="280" y="176" width="50" height="6" rx="3"/><rect x="280" y="200" width="50" height="6" rx="3"/><rect x="280" y="224" width="50" height="6" rx="3"/></g>
    <g fill="#33c28a"><rect x="420" y="128" width="90" height="6" rx="3"/><rect x="420" y="152" width="70" height="6" rx="3"/><rect x="420" y="176" width="100" height="6" rx="3"/><rect x="420" y="200" width="56" height="6" rx="3"/><rect x="420" y="224" width="84" height="6" rx="3"/></g>
  </svg>
</section>

<footer class="section footer">
  <div class="footer-info">
    <div class="logo"><span class="logo-dot"></span>QualiSpan</div>
    <div>(555) 014-2290</div>
    <div class="link">hello@qualispan.example</div>
    <div>1800 Harbor Lane, Suite 4</div>
    <div>Springfield, CA 90000</div>
  </div>
  <div class="footer-col"><h4>Explore</h4><ul><li>Home</li><li>Services</li><li>Speech Vision</li><li>Pricing</li><li>Blog</li><li>Contact Us</li></ul></div>
  <div class="footer-col"><h4>Services</h4><ul><li>Call Review</li><li>Compliance</li><li>Sales Insight</li><li>Agent Training</li><li>Hybrid Scoring</li></ul></div>
  <div class="footer-col"><h4>Links</h4><ul><li>FAQ</li><li>Support</li><li>Careers</li><li>Privacy</li></ul>
    <div class="social"><span></span><span></span><span></span><span></span></div>
  </div>
</footer>
<div class="section copyright">© Copyright 2019 by QualiSpan. All rights reserved.</div>

</body>
</html>
```